Brightpath Home & Upkeep Services, are a company that offers a 'one stop shop' pre-move clean up a

I have already selected a logo which I would like on the front of the business cards along with phone numbers, web address and email which are:
0419586402
www.brightpathhome.com.au
brightpathandupkeep@mailnest.com

On the back of the card I would like to list some of the types of service we offer (clean - move - repairs/maintenance) which are:
CLEAN - windows, gutters, solar panels, driveways/paths, carpets.
MOVE - Small/medium size house/office moves, large item pick-up & delivery, yard clean-up and removal.
General maintenance and repairs.

I would like the blue logo on a gray background.

Thanks

```html
<!DOCTYPE html>
<html lang="en">
<head>
<meta charset="utf-8">
<title>Brightpath Home &amp; Upkeep Services – Business Card</title>
<link rel="stylesheet" href="https://fonts.googleapis.com/css2?family=Exo+2:wght@400;600;800&display=swap">
<style>
  :root {
    --brand-blue: #2a6fbf;
    --light-blue: #5aaee8;
    --ink: #1c1c1c;
    --paper: #ffffff;
    --backdrop: #3a3a3c;
  }
  * { box-sizing: border-box; margin: 0; padding: 0; }
  html, body { width: 1200px; height: 900px; overflow: hidden; }
  body {
    background: var(--backdrop);
    font-family: "Exo 2", sans-serif;
    color: var(--ink);
    position: relative;
  }
  .card {
    position: absolute;
    top: 298px;
    width: 500px;
    height: 304px;
    background: var(--paper);
    overflow: hidden;
    box-shadow: 0 10px 30px rgba(0,0,0,.45);
  }
  .card--front { left: 60px; }
  .card--back { left: 640px; }

  /* front */
  .front-band {
    position: absolute; left: 0; right: 0; bottom: 0;
    height: 20px; background: var(--brand-blue);
  }
  .brand {
    position: absolute; right: 40px; top: 96px;
    display: flex; align-items: center; gap: 10px;
  }
  .brand__mark { width: 16px; height: 16px; background: var(--brand-blue); }
  .brand__name {
    font-weight: 800; font-size: 38px; letter-spacing: .5px;
    color: var(--brand-blue); text-transform: uppercase; line-height: 1;
  }
  .contacts {
    position: absolute; right: 40px; top: 170px;
    list-style: none; text-align: right;
    font-size: 14px; line-height: 24px;
  }
  .contacts li { display: flex; justify-content: flex-end; align-items: center; gap: 8px; }
  .contacts svg { width: 12px; height: 12px; fill: var(--brand-blue); }
  .contacts .web { color: var(--light-blue); }

  /* back */
  .back-top {
    position: absolute; left: 0; right: 0; top: 0;
    height: 150px; background: var(--brand-blue);
  }
  .back-name {
    position: absolute; left: 60px; top: 100px;
    font-weight: 800; font-size: 32px; letter-spacing: .5px;
    color: var(--paper); text-transform: uppercase; line-height: 1;
  }
  .services {
    position: absolute; left: 40px; right: 30px; top: 176px;
    list-style: none; font-size: 13px; line-height: 20px;
  }
  .services strong { font-weight: 600; }
  .services .general { color: var(--light-blue); font-size: 14px; }
</style>
</head>
<body>
  <section class="card card--front" aria-label="Card front">
    <div class="brand">
      <span class="brand__mark"></span>
      <span class="brand__name">Brightpath</span>
    </div>
    <ul class="contacts">
      <li>0419586402
        <svg viewBox="0 0 12 12" aria-hidden="true"><path d="M3 0h6a1 1 0 0 1 1 1v10a1 1 0 0 1-1 1H3a1 1 0 0 1-1-1V1a1 1 0 0 1 1-1zm0 2v7h6V2z"/></svg>
      </li>
      <li>brightpathandupkeep@mailnest.com
        <svg viewBox="0 0 12 12" aria-hidden="true"><path d="M0 2h12v8H0zm1 1v.4l5 3.2 5-3.2V3z"/></svg>
      </li>
      <li class="web">www.brightpathhome.com.au
        <svg viewBox="0 0 12 12" aria-hidden="true"><path d="M6 0a6 6 0 1 0 0 12A6 6 0 0 0 6 0zm0 1.2a4.8 4.8 0 1 1 0 9.6 4.8 4.8 0 0 1 0-9.6zM3 5.4h6v1.2H3z"/></svg>
      </li>
    </ul>
    <div class="front-band"></div>
  </section>

  <section class="card card--back" aria-label="Card back">
    <div class="back-top"></div>
    <div class="back-name">Brightpath</div>
    <ul class="services">
      <li><strong>CLEAN</strong> - windows, gutters, solar panels, driveways/paths, carpets.</li>
      <li><strong>MOVE</strong> - Small/medium size house/office moves, large item pick-up &amp; delivery, yard clean-up and removal.</li>
      <li class="general">General maintenance and repairs.</li>
    </ul>
  </section>
</body>
</html>
```